Poker Card Design for Casino Company

I own a 'Fake' Casino business. We do private and corporate events for our clients all around Australia.

To give my business a more professional look, I want my business logo on my Poker cards for a more professional look.

The face of the cards are quite unique and maybe we can try and incorporate these designs into the back of the cards somehow so the front and back of the cards aren't totally opposite to each other.

I'm not sure if my logo and the face card designs will work together, but let's try! :)

PS. I have 2 other files which couldn't be uploaded:
EPS of logo 4.5MB
PDF of design on the face of the cards 8MB

Target Market(s)

Personal use.

Font styles to use
Decorative
Script

Requirements
Must have
• My logo
Black patterned background, as per the image suggestions I attached
Nice to have
• I would like the design of the face of the cards (attached) somehow merge in with the back of the cards

```html
<!DOCTYPE html>
<html lang="en">
<head>
<meta charset="utf-8">
<title>Silver Ace Events – Card Back</title>
<link href="https://fonts.googleapis.com/css2?family=Oswald:wght@700&display=swap" rel="stylesheet">
<style>
  :root {
    --backdrop: #8e8e8e;
    --card-base: #1b1b1b;
    --card-shade: #262626;
    --card-deep: #121212;
    --gold: #c9a55a;
    --gold-bright: #e8c878;
    --gold-dim: #6b5630;
    --brand-orange: #f5a623;
    --chip-dark: #222222;
  }
  html, body {
    margin: 0;
    padding: 0;
    width: 1200px;
    height: 1199px;
    overflow: hidden;
    background: var(--backdrop);
  }
  .canvas {
    position: relative;
    width: 1200px;
    height: 1199px;
  }
  .card-back {
    position: absolute;
    left: 230px;
    top: 70px;
    width: 740px;
    height: 1040px;
    border-radius: 38px;
    overflow: hidden;
    background: var(--card-base);
  }
  .card-back svg {
    display: block;
    width: 100%;
    height: 100%;
  }
  .brand-name {
    font-family: "Oswald", sans-serif;
    font-weight: 700;
    font-size: 66px;
    letter-spacing: 1px;
    fill: var(--brand-orange);
  }
</style>
</head>
<body>
<main class="canvas">
  <section class="card-back" aria-label="Playing card back">
    <svg viewBox="0 0 740 1040" xmlns="http://www.w3.org/2000/svg">
      <defs>
        <linearGradient id="halftone-tone" x1="0" y1="0" x2="1" y2="1">
          <stop offset="0" stop-color="#3a3020"/>
          <stop offset="0.5" stop-color="#5a4a2a"/>
          <stop offset="1" stop-color="#2e261a"/>
        </linearGradient>
      </defs>

      <!-- background panels -->
      <rect class="panel-base" width="740" height="1040" fill="var(--card-base)"/>
      <polygon class="panel-upper-chevron" points="0,0 740,0 740,140 370,520 0,140" fill="var(--card-shade)"/>
      <polygon class="panel-inner-chevron" points="120,0 620,0 370,250" fill="var(--card-deep)"/>

      <!-- upper gold chevrons -->
      <polyline class="chevron-gold" points="120,0 370,250 620,0" fill="none" stroke="var(--gold-bright)" stroke-width="5"/>
      <polyline class="chevron-gold-thin" points="40,30 370,360 700,30" fill="none" stroke="var(--gold-dim)" stroke-width="3"/>

      <!-- lower halftone bands -->
      <polygon class="halftone-band" role="img" aria-label="Gold dotted halftone pattern band"
               points="0,470 0,760 300,1040 470,1040" fill="url(#halftone-tone)"/>
      <polygon class="halftone-band" role="img" aria-label="Gold dotted halftone pattern band"
               points="740,500 740,760 520,1040 200,1040" fill="url(#halftone-tone)"/>

      <!-- lower gold lines -->
      <line class="line-gold" x1="0" y1="460" x2="480" y2="1040" stroke="var(--gold)" stroke-width="5"/>
      <line class="line-gold" x1="740" y1="490" x2="190" y2="1040" stroke="var(--gold)" stroke-width="5"/>
      <line class="line-gold-thin" x1="0" y1="850" x2="200" y2="1040" stroke="var(--gold-dim)" stroke-width="3"/>
      <line class="line-gold-thin" x1="740" y1="860" x2="560" y2="1040" stroke="var(--gold-dim)" stroke-width="3"/>
      <polyline class="chevron-small" points="280,800 370,710 460,800" fill="none" stroke="var(--gold-dim)" stroke-width="3"/>

      <!-- brand mark -->
      <g class="brand">
        <circle cx="370" cy="520" r="120" fill="var(--chip-dark)"/>
        <text class="brand-name" x="370" y="544" text-anchor="middle">SILVER ACE EVENTS</text>
      </g>
    </svg>
  </section>
</main>
</body>
</html>
```